Personal Business Card

Looking for a clean and modern personal business card. Basically I need something catchy to give to potential clients and people I meet. I do a lot of freelancing (from DJ'ing to wedding videography, but its mostly on the event side of things) so it's more-so about selling myself rather than identifying with a company. I'm starting to meet more people that I want to work with after meeting them so I'm revamping my business cards.

I'm looking for a clean and modern design- I know that's really vague but I'm fine with anything ranging from a symbol to just a fancy version of my name.

Details I need on the front:
Dennis Kowal
dennis@denniskowal-mail.net
(555) 807-2291

On the back I'd like to have something simple like "Nice to have met you today" or "Great meeting you".

UPDATE 9/27 Noon: My apologies for not putting it up before- I'm definitely looking for full color. Doesn't have to be a rainbow but I am looking for the least amount of blank white as possible.

UPDATE 10/1: Really impressed with what I've been getting so far and I'm working on giving everyone feedback- if your design is still up then you're still in the run. Looking for something more unique and modern so please do not post something that looks like a template from Cardloom!

Target Market(s)

Mainly to give to people aged 18-35. Most of my encounters will be casual so the card should have a "young" feeling to it. I rarely do anything in the corporate world so it doesn't have to be boring. It should give the impression that I'm the one they should go to if they need what I do (again it changes every weekend so I'll probably say the "what I do" part.

Industry/Entity Type

Wedding

Requirements
Must have
• Basically the contact information listed above
Nice to have
• I really like the colors Blue, Silver, and Purple. They don't have to necessarily all be there though. I do like the look of polished metal if that makes sense.
Should not have
• A template that resembles card-loom. I'm in a point in my life where I'm working a lot of different markets/areas so the card does not need to have an address or address placeholder.

```html
<!DOCTYPE html>
<html lang="en">
<head>
<meta charset="utf-8">
<title>Dennis Kowal — Business Card</title>
<link rel="stylesheet" href="https://fonts.googleapis.com/css2?family=Montserrat:wght@400;700;800&display=swap">
<style>
  :root {
    --backdrop: #3b3e3d;
    --card-white: #f7f7f5;
    --brand-blue: #1769ad;
    --brand-blue-light: #2a86c9;
    --brand-purple: #8a1fd4;
    --brand-purple-light: #a63de6;
    --ink: #1b1b1b;
  }
  * { margin: 0; padding: 0; box-sizing: border-box; }
  html, body {
    width: 1200px;
    height: 900px;
    overflow: hidden;
    background: var(--backdrop);
    font-family: "Montserrat", sans-serif;
  }
  .card-sheet {
    width: 1200px;
    height: 900px;
    display: flex;
    flex-direction: column;
    align-items: center;
    justify-content: center;
    gap: 60px;
  }
  .card {
    width: 640px;
    height: 366px;
    display: block;
    box-shadow: 0 10px 28px rgba(0, 0, 0, 0.45);
  }
  .card-base { fill: var(--card-white); }
  .band-blue { fill: url(#blueSheen); }
  .band-purple { fill: var(--brand-purple); }
  .band-purple-back { fill: var(--brand-purple-light); }
  .contact-line { font-size: 18.5px; font-weight: 400; fill: var(--ink); letter-spacing: 0.3px; }
  .contact-strong { font-weight: 800; }
  .name-light { font-weight: 400; fill: var(--ink); }
  .name-strong { font-weight: 800; fill: var(--ink); }
  .front-name { font-size: 27px; letter-spacing: 0.5px; }
  .back-name { font-size: 22px; letter-spacing: 0.5px; }
  .greeting { font-size: 33px; font-weight: 800; fill: var(--ink); letter-spacing: 1px; }
  .mark-square { fill: none; stroke: var(--ink); stroke-width: 2.5; }
</style>
</head>
<body>
<main class="card-sheet">

  <svg class="card card-front" viewBox="0 0 640 366" aria-label="Card front">
    <defs>
      <linearGradient id="blueSheen" x1="0" y1="0" x2="1" y2="1">
        <stop offset="0" stop-color="var(--brand-blue)"/>
        <stop offset="0.6" stop-color="var(--brand-blue-light)"/>
        <stop offset="1" stop-color="var(--brand-blue)"/>
      </linearGradient>
    </defs>
    <rect class="card-base" width="640" height="366"/>
    <polygon class="band-purple" points="0,0 640,0 640,226 0,10"/>
    <polygon class="band-blue" points="0,0 640,0 640,213 0,0"/>
    <text class="contact-line" transform="translate(52 50) rotate(18.6)">
      <tspan class="contact-strong">DENNIS</tspan>@DENNISKOWAL-MAIL.NET <tspan class="contact-strong">|</tspan> (555) 807-2291
    </text>
    <rect class="mark-square" x="58" y="200" width="54" height="54"/>
    <text class="front-name" x="58" y="306">
      <tspan class="name-light">DENNIS </tspan><tspan class="name-strong">KOWAL</tspan>
    </text>
  </svg>

  <svg class="card card-back" viewBox="0 0 640 366" aria-label="Card back">
    <rect class="card-base" width="640" height="366"/>
    <polygon class="band-purple-back" points="0,0 220,0 0,220"/>
    <polygon class="band-blue" points="640,20 640,366 294,366"/>
    <text class="back-name" transform="translate(24 222) rotate(-45)">
      <tspan class="name-light">DENNIS </tspan><tspan class="name-strong">KOWAL</tspan>
    </text>
    <text class="greeting" text-anchor="middle" transform="translate(460 188) rotate(-45)">GREAT MEETING YOU</text>
  </svg>

</main>
</body>
</html>
```